Tamsel wine Label, 750ml bottle

We need a wine label that is simple, clean, and timeless. The final project should reflect a premium product. All ideas encouraged. A label that is eye catching and gives of a pristine look. The wine is a Red Blend of Zinfandel, Syrah, Grenache, and Tempranillo. All Californian fruit and hand crafted. The wine is really something special and the label should reflect that. The label must also be able to carry many tiers, the addition of some other labels based around this label may take place in the future.

Target Market(s)

All ideas welcome

Industry/Entity Type

Retail

Font styles to use
Serif

Requirements
Must have
• Open to all ideas.
Nice to have
• An elegant look, simple colors, however, some sort of eye catching effect.
Should not have
• Should not be quirky.

```html
<!DOCTYPE html>
<html lang="en">
<head>
<meta charset="utf-8">
<title>Tamsel – Zinfandel Label Tiers</title>
<link href="https://fonts.googleapis.com/css2?family=Cormorant+Garamond:wght@400;500&display=swap" rel="stylesheet">
<style>
  :root {
    --backdrop: #d9d9d9;
    --paper-white: #f4f4f2;
    --paper-black: #1f1f1f;
    --ink-black: #161616;
    --ink-gold: #c8b57a;
    --ink-silver: #d8d8d8;
    --wine-red: #b0103a;
    --vintage-grey: #8a8a8a;
  }
  * { box-sizing: border-box; margin: 0; padding: 0; }
  html, body {
    width: 1200px;
    height: 800px;
    overflow: hidden;
    background: var(--backdrop);
  }
  .canvas {
    width: 1200px;
    height: 800px;
    display: flex;
    justify-content: center;
    align-items: center;
    gap: 60px;
  }
  .label {
    width: 440px;
    height: 560px;
    display: flex;
    flex-direction: column;
    align-items: center;
    justify-content: center;
    box-shadow: 0 10px 30px rgba(0,0,0,0.18);
  }
  .label--classic { background: var(--paper-white); color: var(--ink-black); }
  .label--reserve { background: var(--paper-black); color: var(--ink-gold); }

  .brand {
    display: flex;
    align-items: center;
    gap: 14px;
  }
  .brand__square {
    width: 14px;
    height: 14px;
    background: currentColor;
  }
  .brand__name {
    font-family: "Cormorant Garamond", serif;
    font-weight: 500;
    font-size: 50px;
    letter-spacing: 4px;
    line-height: 1;
  }
  .varietal {
    margin-top: 110px;
    font-family: "Cormorant Garamond", serif;
    font-weight: 500;
    font-size: 44px;
    letter-spacing: 1px;
    color: var(--wine-red);
    line-height: 1;
  }
  .vintage {
    margin-top: 14px;
    font-family: "Cormorant Garamond", serif;
    font-size: 20px;
    letter-spacing: 10px;
    padding-left: 10px;
    color: var(--vintage-grey);
    line-height: 1;
  }
  .region {
    margin-top: 34px;
    font-family: "Cormorant Garamond", serif;
    font-weight: 500;
    font-size: 22px;
    letter-spacing: 9px;
    padding-left: 9px;
    line-height: 1;
  }
  .label--reserve .region { color: var(--ink-silver); }
</style>
</head>
<body>
<main class="canvas">
  <section class="label label--classic">
    <div class="brand">
      <span class="brand__square"></span>
      <h1 class="brand__name">TAMSEL</h1>
    </div>
    <p class="varietal">ZINFANDEL</p>
    <p class="vintage">2010</p>
    <p class="region">CALIFORNIA</p>
  </section>

  <section class="label label--reserve">
    <div class="brand">
      <span class="brand__square"></span>
      <h1 class="brand__name">TAMSEL</h1>
    </div>
    <p class="varietal">ZINFANDEL</p>
    <p class="vintage">2010</p>
    <p class="region">CALIFORNIA</p>
  </section>
</main>
</body>
</html>
```